Southport Billboard for Hiring more CDL drivers

I need a catch design for a bill board (size 10ft by 36 ft) to catch the attention for semi truck drivers.
In the design I want it to include:
-My company logo along with my website(ridgewaycarriers.com) and my number(803-555-0172) for contact info.
-I also need it to say earn up to $90,000 a year
-I will send a few photos to choose from
-I need the logo to look clean and simple! I don't want it to be cluttered just clean, simple and catchy.!

Target Market(s)

CDL Class A holders
Semi Truck Drivers

Industry/Entity Type

Trucking Company

Font styles to use
Other font styles liked:
• a font to match my logo

Requirements
Must have
• "Make up to $90,000"
"ridgewaycarriers.com"
"803-555-0172"

```html
<!DOCTYPE html>
<html lang="en">
<head>
<meta charset="utf-8">
<title>Ridgeway Carriers – Hiring CDL Drivers Billboard</title>
<link rel="stylesheet" href="https://fonts.googleapis.com/css2?family=Anton&family=Oswald:wght@600;700&family=Montserrat:wght@800&display=swap">
<style>
  :root {
    --page-bg: #3a3a3a;
    --panel-white: #f4f4f4;
    --ink-dark: #1f2420;
    --brand-red: #930b0b;
    --brand-blue: #0d3a86;
    --stripe-red: #d46a6a;
    --stripe-blue: #1e4b9a;
    --white: #ffffff;
    --sky: #dfe6ee;
    --road: #6e7178;
  }
  * { margin: 0; padding: 0; box-sizing: border-box; }
  html, body { width: 1061px; height: 1200px; overflow: hidden; }
  body {
    background: radial-gradient(ellipse at center, #5a5a5a 0%, var(--page-bg) 75%);
    position: relative;
  }
  .billboard {
    position: absolute;
    left: 30px; top: 461px;
    width: 1001px; height: 278px;
    background: var(--panel-white);
    box-shadow: 0 14px 30px rgba(0,0,0,.45);
    overflow: hidden;
  }
  .billboard-shapes { position: absolute; inset: 0; }
  .brand-name {
    position: absolute; left: 36px; top: 22px;
    font-family: "Anton", sans-serif;
    color: var(--ink-dark);
    font-size: 54px; line-height: 0.98;
    letter-spacing: 1px;
    text-transform: uppercase;
  }
  .hiring-label {
    position: absolute; left: 30px; top: 176px;
    font-family: "Oswald", sans-serif; font-weight: 700;
    color: var(--white);
    font-size: 33px; line-height: 44px;
    letter-spacing: 0.2px;
    text-transform: uppercase;
  }
  .contact-phone {
    position: absolute; left: 30px; top: 226px;
    display: flex; align-items: center; gap: 6px;
    font-family: "Montserrat", sans-serif; font-weight: 800;
    color: var(--brand-blue);
    font-size: 29px; line-height: 40px;
  }
  .offer-lead {
    position: absolute; right: 30px; top: 22px;
    font-family: "Anton", sans-serif;
    color: var(--brand-red);
    font-size: 44px; line-height: 54px;
    text-transform: uppercase;
  }
  .offer-amount {
    position: absolute; right: 30px; top: 74px;
    font-family: "Anton", sans-serif;
    color: var(--white);
    font-size: 76px; line-height: 96px;
    text-shadow: 0 3px 0 #9aa3b0, 0 5px 6px rgba(0,0,0,.45);
  }
  .offer-period {
    position: absolute; right: 30px; top: 170px;
    font-family: "Oswald", sans-serif; font-weight: 700;
    color: #111;
    font-size: 36px; line-height: 44px;
    text-transform: uppercase;
  }
  .contact-web {
    position: absolute; right: 28px; top: 219px;
    display: flex; align-items: center; gap: 8px;
    font-family: "Oswald", sans-serif; font-weight: 600;
    color: var(--white);
    font-size: 25px; line-height: 40px;
  }
  .icon { flex: none; }
</style>
</head>
<body>
  <section class="billboard" aria-label="Ridgeway Carriers driver recruitment billboard">
    <svg class="billboard-shapes" width="1001" height="278" viewBox="0 0 1001 278">
      <defs>
        <linearGradient id="photoTone" x1="0" y1="0" x2="0" y2="1">
          <stop offset="0" stop-color="var(--sky)"/>
          <stop offset="0.45" stop-color="#9aa6b4"/>
          <stop offset="0.7" stop-color="#7b8088"/>
          <stop offset="1" stop-color="var(--road)"/>
        </linearGradient>
      </defs>
      <polygon class="truck-photo" role="img" aria-label="Photo of two semi trucks, a blue one and a red one, parked side by side"
               points="252,0 640,0 737,278 332,278" fill="url(#photoTone)"/>
      <polygon class="stripe-blue" points="240,0 252,0 332,278 320,278" fill="var(--stripe-blue)"/>
      <polygon class="stripe-red" points="640,0 652,0 749,278 737,278" fill="var(--stripe-red)"/>
      <polygon class="band-hiring" points="0,174 313,174 330,221 0,221" fill="var(--brand-red)"/>
      <polygon class="band-amount" points="662,75 1001,75 1001,170 693,170" fill="var(--brand-blue)"/>
      <polygon class="band-web" points="686,218 1001,218 1001,260 700,260" fill="var(--brand-red)"/>
    </svg>

    <h1 class="brand-name">Ridgeway<br>Carriers</h1>
    <p class="hiring-label">Hiring CDL Drivers</p>
    <p class="contact-phone">
      <svg class="icon" width="26" height="26" viewBox="0 0 26 26" aria-hidden="true">
        <circle cx="13" cy="13" r="12" fill="var(--brand-red)" stroke="var(--brand-blue)" stroke-width="2"/>
        <path d="M9 7c1-.6 1.8 0 2.3 1.2l.6 1.6c.3.8-.2 1.3-.8 1.8.5 1.5 1.6 2.7 3 3.4.5-.6 1-1.1 1.8-.8l1.6.6c1.2.5 1.6 1.4 1 2.3-.8 1.2-2 1.6-3.4 1.1C11 16.8 8.5 14 7.6 10.8 7.2 9.2 7.8 7.8 9 7z" fill="var(--white)"/>
      </svg>
      803-555-0172
    </p>

    <p class="offer-lead">Make up to</p>
    <p class="offer-amount">$90,000</p>
    <p class="offer-period">A Year</p>
    <p class="contact-web">
      <svg class="icon" width="22" height="22" viewBox="0 0 22 22" aria-hidden="true" fill="none" stroke="var(--white)" stroke-width="1.6">
        <circle cx="11" cy="11" r="9.5"/>
        <ellipse cx="11" cy="11" rx="4" ry="9.5"/>
        <line x1="1.5" y1="11" x2="20.5" y2="11"/>
        <path d="M3.5 6h15M3.5 16h15"/>
      </svg>
      ridgewaycarriers.com
    </p>
  </section>
</body>
</html>
```